Design me a minimalist business card

I need a minimalist, one-sided business card with name, email, phone number, location (university)

I am leaning towards a dark theme, but open to other ideas. Will probably print on matte paper with metallic text.

```html
<!DOCTYPE html>
<html lang="en">
<head>
<meta charset="UTF-8">
<title>Minimalist Business Card</title>
<link rel="stylesheet" href="https://fonts.googleapis.com/css2?family=Open+Sans:wght@300;400;700&display=swap">
<style>
  :root {
    --page-bg: #e4e1dc;
    --card-top: #444547;
    --card-bottom: #2b2c2e;
    --text-main: #e8e8e8;
    --text-soft: #b9babc;
    --text-label: #ffffff;
  }
  * { box-sizing: border-box; margin: 0; padding: 0; }
  html, body {
    width: 1200px;
    height: 1023px;
    overflow: hidden;
    background: var(--page-bg);
    font-family: "Open Sans", Arial, sans-serif;
  }
  .canvas {
    width: 1200px;
    height: 1023px;
    display: flex;
    align-items: center;
    justify-content: center;
  }
  .business-card {
    position: relative;
    width: 900px;
    height: 514px;
    background: linear-gradient(160deg, var(--card-top) 0%, var(--card-bottom) 100%);
    box-shadow: 0 18px 40px rgba(0,0,0,0.25);
  }
  .identity {
    position: absolute;
    left: 72px;
    bottom: 120px;
  }
  .identity .name {
    font-size: 44px;
    font-weight: 300;
    color: var(--text-main);
    letter-spacing: 0.5px;
    line-height: 1.1;
  }
  .identity .role {
    font-size: 26px;
    font-weight: 300;
    color: var(--text-soft);
    margin-top: 4px;
  }
  .contact {
    position: absolute;
    left: 560px;
    top: 78px;
    font-size: 24px;
    font-weight: 300;
    color: var(--text-main);
    line-height: 1.45;
    white-space: nowrap;
  }
  .contact .label,
  .address .label {
    font-weight: 700;
    color: var(--text-label);
  }
  .contact .label { display: inline-block; width: 34px; }
  .address {
    position: absolute;
    left: 560px;
    top: 290px;
    font-size: 24px;
    font-weight: 300;
    color: var(--text-main);
    line-height: 1.45;
    white-space: nowrap;
  }
</style>
</head>
<body>
  <main class="canvas">
    <section class="business-card">
      <div class="identity">
        <p class="name">Daniel Hart</p>
        <p class="role">President</p>
      </div>
      <div class="contact">
        <p><span class="label">T:</span> 555-318-2047</p>
        <p><span class="label">M:</span> hello@dhartmail.com</p>
      </div>
      <div class="address">
        <p class="label">Address:</p>
        <p>Westbrook University Campus</p>
      </div>
    </section>
  </main>
</body>
</html>
```